NURSING: RISING PAST THE SHADOWED SILL

Size of the book cover: 140 x 215 mms

I need a cover for the 30,000 word book I have just written. It is a positive take on what I think nursing is and what it needs to be in the future. It is also my story of being nursed and of being a nurse.

My dream is that nurses honor themselves; that they look to the future with confidence and intelligence and that care continues to be delivered with compassionate person centeredness.

I define nursing as a professional workforce which, with probity, prevent or relieve distress; provide compassionate, safe, excellent care; and which contributes to the organization of healthcare.

The name comes from a Biblical parable Corlan 3:7-9. If a light is hidden under a bushel (basket) it is barely seen. If it is lit out from the basket it is clearly seen. As nurses we must continue to take up our mantel and ensure our light is seen and that it continues to shine the way we want it to.

As nurses we each take up our own lantern of caring, each in our own ways. To walk more brightly in our own paths of service.

The final design should show the specialness of nursing.

Target Market(s)

Nurses present, past and future

Industry/Entity Type

Healthcare

Font styles to use
Sans Serif
Other font styles liked:
• Whatever you think will suit

Colors
ec1f27
0393ce
9bcb3c

Requirements
Must have
• Be friendly, calming.
• NB: I am not sure whether the title should be in uppercase or not. Nursing could be uppercase and rising past the shadowed sill could be lower case. I leave it to you experienced people
Nice to have
• Something that depicts nursing...or is suggestive of nursing and the specialness of the work we do. How we bring our light to our patients as we 'hold them in the palms of out hands' and care for them. How they honor us by allowing us into their lives. Our rich past and out history allows us to be who we are today and we look to the future with confidence and hope
• I like rich colors, eg the color type you might find on a stained glass window in a church - rich emerald green or rich crimson red or the deep blue of a nurses cape
Should not have
• A dark cover
• clutter
• Religious overtone
• I have chosen three colors but they are not in the shading I would like - see above

```html
<!DOCTYPE html>
<html lang="en">
<head>
<meta charset="utf-8">
<title>Nursing: Rising Past the Shadowed Sill — Book Cover</title>
<link rel="stylesheet" href="https://fonts.googleapis.com/css2?family=Arimo:wght@400&family=Montserrat:wght@700&family=Nunito+Sans:wght@400&family=Open+Sans:wght@400;700&display=swap">
<style>
  :root {
    --cape-blue: #0393ce;
    --title-blue: #0a93d1;
    --crimson: #ec1f27;
    --mist: #cce3df;
    --ink: #111111;
    --body-ink: #1e1e1e;
    --subtitle-grey: #3a3a3a;
    --paper: #ffffff;
  }
  * { margin: 0; padding: 0; box-sizing: border-box; }
  html, body {
    width: 1200px; height: 860px; overflow: hidden; background: var(--paper);
  }
  .cover {
    position: relative; width: 1200px; height: 860px; overflow: hidden; background: var(--paper);
  }
  .cover-shapes { position: absolute; inset: 0; }

  .back-blurb {
    position: absolute; left: 153px; top: 47px; width: 370px;
    font-family: "Nunito Sans", Arial, sans-serif;
    font-size: 12.4px; line-height: 16.8px; color: var(--body-ink);
  }
  .back-blurb p { margin-bottom: 16.8px; }
  .back-blurb p.tight { margin-bottom: 0; }
  .back-blurb .line { display: block; white-space: nowrap; }

  .spine-watermark {
    position: absolute; left: 826px; top: 40px;
    transform-origin: 0 0; transform: rotate(90deg);
    font-family: "Montserrat", Arial, sans-serif; font-weight: 700;
    font-size: 200px; line-height: 1; color: var(--mist);
    letter-spacing: -4px; white-space: nowrap;
  }
  .author-name {
    position: absolute; left: 742px; top: 136px;
    transform-origin: 0 0; transform: rotate(90deg);
    font-family: "Montserrat", Arial, sans-serif; font-weight: 700;
    font-size: 72px; line-height: 1; color: var(--ink);
    white-space: nowrap; letter-spacing: -1px;
  }

  .lantern-quote {
    position: absolute; left: 799px; top: 166px; width: 380px;
    font-family: "Arimo", Arial, sans-serif; color: var(--ink);
  }
  .lantern-quote span { display: block; white-space: nowrap; }
  .lantern-quote .line-one { font-size: 11.5px; padding-left: 21px; line-height: 16px; }
  .lantern-quote .line-two { font-size: 13px; padding-left: 153px; line-height: 16px; }
  .lantern-quote .line-three { font-size: 16.8px; line-height: 20px; }

  .book-title {
    position: absolute; left: 882px; top: 397px;
    font-family: "Open Sans", Arial, sans-serif;
  }
  .book-title .title-main {
    display: block; font-weight: 700; font-size: 75px; line-height: 1;
    letter-spacing: -2.5px; color: var(--title-blue);
  }
  .book-title .title-sub {
    display: block; font-weight: 400; font-size: 16.5px; line-height: 1;
    color: var(--subtitle-grey); margin-top: -4px; padding-left: 3px;
  }
</style>
</head>
<body>
<main class="cover">
  <svg class="cover-shapes" width="1200" height="860" viewBox="0 0 1200 860" aria-hidden="true">
    <rect class="back-band-blue" x="0" y="0" width="84" height="860" fill="var(--cape-blue)"/>
    <rect class="back-band-red" x="84" y="0" width="14" height="860" fill="var(--crimson)"/>
    <circle class="back-light" cx="42" cy="680" r="24" fill="var(--crimson)"/>
    <circle class="front-light" cx="906" cy="680" r="56" fill="var(--crimson)"/>
    <path class="front-arc" d="M640 828 Q900 760 1200 800 L1200 826 Q900 792 640 852 Z" fill="var(--crimson)"/>
  </svg>

  <div class="spine-watermark" aria-hidden="true">nursing</div>

  <section class="back-blurb">
    <p>
      <span class="line">Nursing is seldom expressed the way that it is in this book.</span>
      <span class="line">It is written by a person who has been nursed or nursing all</span>
      <span class="line">her life and it is recounted with honesty and candour.</span>
      <span class="line">Every reader will find something to take from this narrative</span>
      <span class="line">and nurses will no doubt see something of their own life</span>
      <span class="line">mirrored in the many anecdotes and stories.</span>
    </p>
    <p>
      <span class="line">Nursing: Rising past the shadowed sill is a book which brings</span>
      <span class="line">into the light the authors rich experience of the world and</span>
      <span class="line">work of nursing. Through its words it subtly challenges</span>
      <span class="line">individual nurses to think deeply about what ‘being a nurse’</span>
      <span class="line">means to them.</span>
    </p>
    <p>
      <span class="line">What nurses do is a very big deal. Nurses choose to be</span>
      <span class="line">nurses. No one tells them they have to do it but for some</span>
      <span class="line">reason they decide to. The people they care for honour them</span>
      <span class="line">by allowing them into their lives at what can be the most</span>
      <span class="line">vulnerable and dramatic times of their life. How nurses</span>
      <span class="line">position themselves, how they ‘walk’ with their patients, how</span>
      <span class="line">they connect and care for them has consequences both for</span>
      <span class="line">those in their care and for themselves.</span>
    </p>
    <p>
      <span class="line">One of nursing’s unique realities is that the work crosses</span>
      <span class="line">normal social boundaries. It is work that is not easily talked</span>
      <span class="line">about outside of nursing, and the support nurses provide</span>
      <span class="line">for each other is important in enabling them to remain</span>
      <span class="line">healthy and able.</span>
    </p>
    <p>
      <span class="line">Nursing has a rich history. Adela Marchwood lit her</span>
      <span class="line">lantern of caring more a then a century ago. The light</span>
      <span class="line">from that lantern continues to glow and it is relit every</span>
      <span class="line">moment of everyday by nurses all around the world as</span>
      <span class="line">they go about their work.</span>
    </p>
    <p>
      <span class="line">This book is more than just a story of nursing. It is the story</span>
      <span class="line">and chronology of a professional life, intermingled with the</span>
      <span class="line">telling of personal accounts and experiences. It also includes</span>
      <span class="line">some special thoughts on nursing now and into the future.</span>
      <span class="line">Nursing in the present day, presents many new challenges</span>
      <span class="line">and opportunities. The workforce is one which adapts well</span>
      <span class="line">to new ideas and situations.</span>
      <span class="line">The future of nursing is in nurses hands and as such it can look</span>
      <span class="line">to the future with confidence and pride.</span>
    </p>
    <p class="tight">
      <span class="line">The writer salutes nurses everywhere.</span>
    </p>
  </section>

  <div class="author-name">Maren Tolliver</div>

  <blockquote class="lantern-quote">
    <span class="line-one">“We each take up our own lantern of caring,</span>
    <span class="line-two">each in our own ways,</span>
    <span class="line-three">to walk more brightly in our own path of service”</span>
  </blockquote>

  <h1 class="book-title">
    <span class="title-main">nursing</span>
    <span class="title-sub">rising past the shadowed sill</span>
  </h1>
</main>
</body>
</html>
```